International business needs business cards

Our company, RUV Partners Inc. is in the business of supplying a range construction products with particular emphasis on CEMENT. We have developed our own brand - BOREAL SUPPLIES - with which to infiltrate the market. We are launching our brand of cement (BOREAL Type IS Cement) into the Caribbean which is unlike anything this market has ever seen. A monopoly has existed here for the past 60-odd years and the market has now opened to allow the importation of other brands and consumers are anxious and ready for change/improvement. We are very excited to be launching and want to make a great first impression. We will be conducting workshops and seminars (from government level to the hardware store owners) and we want our business card to give us the strong, confident introduction that we need.

Target Market(s)

construction; builders; engineers; home owners

Industry/Entity Type

Construction

Contact Information for Business Card

Melvina Tosh
CEO
cell # 1 868 5550147
Ground floor,Palmetto Plaza Suite 2473
George Town,Grand Cayman
Cayman Islands,KY1-1990
EMAIL: m.tosh@ruvpartnersinc.example
web site ruvpartnersinc.example

COMPANY: skype info ruv.partners.example

second card
Hester Quimby-Tosh
CFO
CELL# 1 868 555 0382
George Town,Grand Cayman
Cayman Islands,KY1-1990
EMAIL: h.quimbytosh@ruvpartnersinc.example
website ruvpartnersinc.example

Requirements
Must have
• Business cards must display BOTH logos - RUV is the company and BOREAL is the brand.

```html
<!DOCTYPE html>
<html lang="en">
<head>
<meta charset="utf-8">
<title>RUV Partners Inc. — Business Card</title>
<link rel="stylesheet" href="https://fonts.googleapis.com/css2?family=Source+Sans+3:wght@400;600;700&display=swap">
<style>
  :root {
    --backdrop: #3b332f;
    --card-white: #f7f6f4;
    --brand-red: #8b1a1e;
    --brand-red-dark: #6e1417;
    --ink: #1f1f1f;
    --ink-soft: #3a3a3a;
    --seal-grey: #8a8a8a;
    --on-red: #ffffff;
  }
  * { box-sizing: border-box; margin: 0; padding: 0; }
  html, body { width: 1200px; height: 844px; overflow: hidden; }
  body {
    background: var(--backdrop);
    font-family: "Source Sans 3", Arial, sans-serif;
    color: var(--ink);
    display: flex;
    align-items: center;
    justify-content: center;
    gap: 60px;
  }
  .card {
    width: 520px;
    height: 300px;
    position: relative;
    border-radius: 3px;
    box-shadow: 0 10px 24px rgba(0,0,0,0.4);
  }
  .card--front { background: var(--card-white); }
  .card--back {
    background: linear-gradient(135deg, var(--brand-red) 0%, var(--brand-red-dark) 100%);
  }

  .company-mark {
    position: absolute;
    display: flex;
    align-items: center;
    gap: 10px;
  }
  .company-mark__square {
    width: 44px;
    height: 44px;
    background: var(--brand-red);
    flex: none;
  }
  .company-mark__name {
    font-weight: 700;
    font-size: 21px;
    letter-spacing: 0.5px;
    line-height: 1;
    text-transform: uppercase;
  }
  .card--front .company-mark { top: 38px; right: 42px; }
  .card--front .company-mark__name { color: var(--ink); }
  .card--back .company-mark { top: 118px; right: 40px; }
  .card--back .company-mark__name { color: var(--on-red); font-size: 26px; }

  .brand-seal {
    position: absolute;
    right: 54px;
    top: 138px;
    width: 40px;
    height: 40px;
    border-radius: 50%;
    background: var(--seal-grey);
  }

  .contact {
    position: absolute;
    left: 34px;
    bottom: 28px;
  }
  .contact__name {
    color: var(--brand-red);
    font-size: 19px;
    font-weight: 600;
    line-height: 1.1;
  }
  .contact__title {
    font-size: 13px;
    color: var(--ink-soft);
    margin-bottom: 14px;
  }
  .contact__address {
    font-size: 13.5px;
    line-height: 1.35;
    color: var(--ink-soft);
    margin-bottom: 10px;
    font-style: normal;
  }
  .contact__list { list-style: none; }
  .contact__item {
    display: flex;
    align-items: center;
    gap: 8px;
    font-size: 13.5px;
    line-height: 1.5;
    color: var(--ink-soft);
  }
  .contact__icon { width: 11px; height: 11px; flex: none; }
</style>
</head>
<body>

  <section class="card card--front" aria-label="Business card front">
    <div class="company-mark">
      <span class="company-mark__square"></span>
      <span class="company-mark__name">RUV Partners Inc.</span>
    </div>

    <span class="brand-seal" role="img" aria-label="BOREAL Supplies brand seal"></span>

    <div class="contact">
      <p class="contact__name">Melvina Tosh</p>
      <p class="contact__title">CEO</p>
      <address class="contact__address">
        Ground floor, Palmetto Plaza Suite 2473<br>
        George Town, Grand Cayman<br>
        Cayman Islands, KY1-1990
      </address>
      <ul class="contact__list">
        <li class="contact__item">
          <svg class="contact__icon" viewBox="0 0 12 12" aria-hidden="true">
            <path fill="var(--brand-red)" d="M2.5 1h2l1 3-1.3 1a6 6 0 0 0 2.8 2.8L8 6.5l3 1v2a1.5 1.5 0 0 1-1.5 1.5A8.5 8.5 0 0 1 1 2.5 1.5 1.5 0 0 1 2.5 1z"/>
          </svg>
          1 868 5550147
        </li>
        <li class="contact__item">
          <svg class="contact__icon" viewBox="0 0 12 12" aria-hidden="true">
            <rect x="0.5" y="2" width="11" height="8" fill="var(--brand-red)"/>
            <path d="M0.5 2.5 6 6.5l5.5-4" fill="none" stroke="#fff" stroke-width="1"/>
          </svg>
          m.tosh@ruvpartnersinc.example
        </li>
        <li class="contact__item">
          <svg class="contact__icon" viewBox="0 0 12 12" aria-hidden="true">
            <circle cx="6" cy="6" r="5.5" fill="var(--brand-red)"/>
            <path d="M0.5 6h11M6 0.5c-2.5 3-2.5 8 0 11M6 0.5c2.5 3 2.5 8 0 11" fill="none" stroke="#fff" stroke-width="0.8"/>
          </svg>
          www.ruvpartnersinc.example
        </li>
      </ul>
    </div>
  </section>

  <section class="card card--back" aria-label="Business card back">
    <div class="company-mark">
      <span class="company-mark__name">RUV Partners Inc.</span>
    </div>
  </section>

</body>
</html>
```